Corvane Strategy Partners Marketing Audit Teaser

Design a 1-page (2-sided) teaser on the Corvane Strategy Partners Marketing Audit. A Project Brief; Copy document; logo file; and picture file will be provided to further detail what is required. Additional logo files are available, if needed, depending on the designers recommendations.

```html
<!DOCTYPE html>
<html lang="en">
<head>
<meta charset="utf-8">
<title>Corvane Strategy Partners – Marketing Audit Teaser</title>
<link rel="stylesheet" href="https://fonts.googleapis.com/css2?family=Cinzel:wght@600;700&family=Montserrat:ital,wght@0,400;0,500;0,600;0,700;1,400&display=swap">
<style>
  :root {
    --backdrop: #cfcfcf;
    --paper: #f3f4f3;
    --forest: #165132;
    --forest-soft: #376a4c;
    --ink: #1b1b1b;
    --white: #ffffff;
    --photo-tone: #8a8f96;
  }
  * { box-sizing: border-box; margin: 0; padding: 0; }
  html, body { width: 1200px; height: 818px; overflow: hidden; }
  body {
    background: var(--backdrop);
    font-family: "Montserrat", Arial, sans-serif;
    color: var(--ink);
    position: relative;
  }
  .side-label {
    position: absolute; top: 34px;
    font-size: 11px; letter-spacing: 5px; color: var(--ink);
    transform: translateX(-50%);
    white-space: nowrap;
  }
  .sheet {
    position: absolute; top: 64px; width: 560px; height: 725px;
    background: var(--paper); overflow: hidden;
  }
  .sheet--front { left: 36px; }
  .sheet--back { left: 613px; }

  /* Front */
  .hero {
    position: absolute; left: 0; top: 0; width: 560px; height: 443px;
    background: var(--forest); color: var(--white);
  }
  .hero__tagline {
    position: absolute; right: 42px; top: 57px;
    font-size: 6.6px; letter-spacing: 3.2px; line-height: 8.6px; text-align: right;
  }
  .hero__brand {
    position: absolute; left: 18px; width: 260px; top: 128px;
    font-size: 18px; font-weight: 500; text-align: center; letter-spacing: 0.3px;
  }
  .hero__brand-mark {
    display: block; width: 34px; height: 34px; margin: 0 auto 12px;
    border: 2px solid var(--white);
  }
  .hero__headline {
    position: absolute; left: 62px; top: 217px;
    font-family: "Cinzel", "Times New Roman", serif; font-weight: 700;
    font-size: 31.5px; line-height: 31px; letter-spacing: 0.2px;
  }
  .hero__lede {
    position: absolute; left: 103px; top: 393px; width: 320px;
    font-size: 10.6px; line-height: 13.5px; letter-spacing: 0.3px;
  }
  .front-body {
    position: absolute; left: 62px; top: 455px; width: 436px;
    font-size: 9.3px; line-height: 12.8px; text-align: justify;
  }
  .front-body p + p { margin-top: 12.8px; }
  .front-body strong, .back-body strong { font-weight: 700; }
  .rule {
    position: absolute; left: 62px; top: 680px; width: 436px; height: 1.5px;
    background: var(--forest);
  }
  .closing {
    position: absolute; left: 0; width: 560px; top: 687px;
    text-align: center; font-size: 9.8px; line-height: 11.6px;
  }
  .closing strong { font-weight: 700; display: block; }

  /* Back */
  .back-title {
    position: absolute; left: 0; width: 560px; top: 48px; text-align: center;
    font-weight: 600; letter-spacing: 0.5px;
  }
  .back-title__main { display: block; font-size: 23.5px; line-height: 28px; }
  .back-title__sub { display: block; font-size: 18.5px; line-height: 24px; }
  .back-body {
    position: absolute; left: 63px; width: 435px;
    font-size: 9.4px; line-height: 12.8px; text-align: justify;
  }
  .back-body h2 { font-size: 12.8px; font-weight: 700; line-height: 15px; margin-bottom: 2px; text-align: left; }
  .back-body h3 { font-size: 10.4px; font-weight: 700; line-height: 13px; margin-bottom: 3px; text-align: left; }
  .back-body ul { list-style: none; }
  .back-body li { position: relative; padding-left: 11px; }
  .back-body li::before { content: "•"; position: absolute; left: 3px; }
  .sec-what { top: 125px; }
  .sec-why { top: 212px; }
  .sec-when { top: 326px; }
  .audit-columns { display: flex; gap: 16px; margin-top: 6px; }
  .audit-columns__col { width: 198px; }
  .audit-columns__col--pe { width: 236px; }
  .sec-included { top: 480px; text-align: left; }
  .callout {
    position: absolute; left: 70px; top: 588px; width: 313px; height: 87px;
    background: var(--forest-soft); color: var(--white);
    display: flex; align-items: center; justify-content: center; text-align: center;
    font-size: 11.6px; line-height: 13px; letter-spacing: 0.5px;
  }
  .founder-photo {
    position: absolute; left: 418px; top: 535px; width: 73px; height: 99px;
    background: linear-gradient(180deg, #e9eaec 0%, #b9bcc2 45%, #2f3440 100%);
  }
  .founder {
    position: absolute; left: 387px; width: 130px; top: 642px; text-align: center;
  }
  .founder__name { font-size: 8.8px; font-weight: 700; letter-spacing: 0.3px; }
  .founder__role { font-size: 5.2px; letter-spacing: 2.4px; line-height: 7px; }
  .founder__quote { font-size: 6.8px; font-style: italic; line-height: 8px; }
</style>
</head>
<body>
  <div class="side-label" style="left:311px">Front Side</div>
  <div class="side-label" style="left:893px">Back Side</div>

  <section class="sheet sheet--front">
    <div class="hero">
      <div class="hero__tagline">MARKETING CLARITY.<br>GROWTH UNLOCKED.</div>
      <div class="hero__brand"><span class="hero__brand-mark"></span>Corvane Strategy Partners</div>
      <h1 class="hero__headline">IF YOU DON’T KNOW<br>WHERE YOU ARE,<br>HOW CAN YOU GET<br>TO WHERE YOU<br>WANT TO BE?</h1>
      <p class="hero__lede">Now, leading firms are applying that same rigor to Marketing—the engine of growth.</p>
    </div>
    <div class="front-body">
      <p>Companies have relied on <strong>financial audits</strong> for decades to confirm company performance, uncover risks, and guide decision making. More recently, leading companies and Private Equity firms are applying the same rigor to <strong>Marketing</strong>—the very engine of revenue growth.</p>
      <p>Corvane’s proprietary Marketing Audit is a <strong>comprehensive, objective assessment</strong> of your company’s marketing effectiveness across 29 practice areas. It identifies what you’re doing well, where there are gaps, and what’s missing entirely—delivering actionable, prioritized recommendations, segmented by timeframe, designed to drive measurable near- and long-term growth.</p>
      <p>Without a Marketing Audit, a company risks undermining its growth trajectory and ultimate enterprise value. Misaligned strategies drain resources, ineffective campaigns dilute returns, and competitors gain ground while leadership operates on incomplete information. Instead of running on data and clarity, the business runs on assumptions—an invisible drag that erodes performance today and jeopardizes exit value tomorrow.</p>
    </div>
    <div class="rule"></div>
    <div class="closing"><strong>Discover where your Marketing really stands.</strong>www.CorvaneStrategy.com</div>
  </section>

  <section class="sheet sheet--back">
    <h1 class="back-title">
      <span class="back-title__main">THE CORVANE MARKETING AUDIT:</span>
      <span class="back-title__sub">CLEAR. CREDIBLE. ACTIONABLE.</span>
    </h1>
    <div class="back-body sec-what">
      <h2>What Is a Marketing Audit?</h2>
      <p>A structured review of all marketing practices, programs, and performance. The audit benchmarks your company against best practices, highlights strengths and weaknesses, and provides a <strong>roadmap for improvement</strong>. It is as rigorous as a financial audit, but focused on Marketing clarity, alignment, and ROI.</p>
    </div>
    <div class="back-body sec-why">
      <h2>Why Companies Need a Marketing Audit</h2>
      <p>Marketing is often fragmented, underfunded, or misaligned with business strategy. Corvane’s Marketing Audit delivers an <strong>unbiased view</strong> of where your Marketing stands today—and how to maximize its impact tomorrow. For executives and investors, it replaces guesswork with actionable insights and clear next steps to optimize resource allocation, enhance customer engagement, ensuring a strong competitive position and a higher return on marketing spend.</p>
    </div>
    <div class="back-body sec-when">
      <h2>When to Conduct a Marketing Audit</h2>
      <div class="audit-columns">
        <div class="audit-columns__col">
          <h3>For Private Companies:</h3>
          <ul>
            <li>When preparing for growth or new market entry.</li>
            <li>When revenue growth has stalled, competitive threats increase, or leadership wants clarity before a major Marketing spend, strategy shift, or rebranding.</li>
          </ul>
        </div>
        <div class="audit-columns__col audit-columns__col--pe">
          <h3>For Private Equity Portfolio Companies:</h3>
          <ul>
            <li><strong>Pre-Closing Due Diligence:</strong> Marketing effectiveness assessment prior to investment.</li>
            <li><strong>Post-Closing 100-Day Plan:</strong> Marketing alignment and integration as a cornerstone to accelerate revenue and maximize enterprise value.</li>
            <li><strong>During Investment Period:</strong> When growth has stalled or when Sales and Marketing functions are being reassessed or overhauled.</li>
          </ul>
        </div>
      </div>
    </div>
    <div class="back-body sec-included">
      <h2>What’s Included</h2>
      <ul style="margin-top:4px">
        <li>Analysis of <strong>29+ Marketing practice areas</strong></li>
        <li>Clear picture of what’s being done <strong>right, not so right, or not at all</strong></li>
        <li><strong>Prioritized recommendations</strong> with realistic timeframes</li>
        <li>Alignment with <strong>executive and financial goals</strong></li>
        <li>Delivery of an <strong>actionable roadmap</strong> for measurable growth</li>
      </ul>
    </div>
    <div class="callout">The Marketing Audit<br>from Corvane Strategy Partners<br>is the essential first step<br>toward driving sustainable growth.</div>
    <div class="founder-photo" role="img" aria-label="Portrait photo of the founder"></div>
    <div class="founder">
      <div class="founder__name">DANIEL ASHWORTH</div>
      <div class="founder__role">FOUNDER</div>
      <div class="founder__quote">“A marketer<br>with an investor’s mindset.”</div>
    </div>
    <div class="closing"><strong>Schedule a conversation today.</strong>www.CorvaneStrategy.com</div>
  </section>
</body>
</html>
```